Gourmet Restaurant Coffee Cup Print Design

We would like to redesign our coffee cup for our restaurant chain. Please visit our website at: www.dorvanti.ca.

Disposable Cup should be bilingual in English and French. We will provide translations. One side is to be french and the other English.

I have uploaded also the files that were provided to us by the cup manufacturer. These templates have all the necessary instructions.

Target Market(s)

Business Professionals, Millenials

Industry/Entity Type

Restaurant

Font styles to use
Serif
Sans Serif
Script

Requirements
Must have
• our entire logo or only the "DORVANTI'S" word in the logo.
• We are looking for 4 cup sizes with the same design but maybe a distinguishing color in each size of cup.
• We can provide cup templates in PDF along with full manufacturer instructions.
• We're looking for a simple clean design with a predominantly white background. The lid of the cup is white.
Nice to have
• Our motto or tag line is:
• A world of taste
Should not have
• photos only use illustrations

```html
<!DOCTYPE html>
<html lang="en">
<head>
<meta charset="utf-8">
<title>Dorvanti's — Cup Wrap</title>
<link rel="stylesheet" href="https://fonts.googleapis.com/css2?family=Bitter:wght@900&family=Archivo+Black&display=swap">
<style>
  :root {
    --paper: #ffffff;
    --green-deep: #0b6637;
    --green-soft: #9ec5b1;
    --fold-line: #8a8a8a;
  }
  html, body {
    margin: 0;
    padding: 0;
    overflow: hidden;
    background: var(--paper);
  }
  .cup-wrap {
    position: relative;
    width: 1200px;
    height: 630px;
    overflow: hidden;
    background: var(--paper);
  }
  .backdrop-word {
    position: absolute;
    margin: 0;
    font-family: "Bitter", Georgia, serif;
    font-weight: 900;
    font-size: 260px;
    line-height: 1;
    letter-spacing: -4px;
    color: var(--green-soft);
    white-space: nowrap;
  }
  .backdrop-word--top {
    left: 132px;
    top: -95px;
  }
  .backdrop-word--bottom {
    right: 8px;
    top: 452px;
  }
  .fold-line {
    position: absolute;
    left: 600px;
    top: 0;
    width: 1px;
    height: 630px;
    background: var(--fold-line);
  }
  .brand-name {
    position: absolute;
    left: 0;
    width: 1200px;
    top: 287px;
    margin: 0;
    text-align: center;
    font-family: "Bitter", Georgia, serif;
    font-weight: 900;
    font-size: 46px;
    line-height: 1;
    letter-spacing: -0.5px;
    color: var(--green-deep);
  }
  .tagline {
    position: absolute;
    top: 368px;
    margin: 0;
    font-family: "Archivo Black", "Arial Black", sans-serif;
    color: var(--green-deep);
    line-height: 0.9;
    letter-spacing: -0.5px;
  }
  .tagline--en {
    right: 622px;
    font-size: 35px;
  }
  .tagline--fr {
    left: 622px;
    top: 373px;
    font-size: 29px;
    line-height: 1;
  }
</style>
</head>
<body>
  <main class="cup-wrap">
    <p class="backdrop-word backdrop-word--top" aria-hidden="true">DORV</p>
    <p class="backdrop-word backdrop-word--bottom" aria-hidden="true">ANTI'S</p>
    <div class="fold-line" aria-hidden="true"></div>
    <h1 class="brand-name">DORVANTI'S</h1>
    <p class="tagline tagline--en" lang="en">A world<br>of taste</p>
    <p class="tagline tagline--fr" lang="fr">Un monde<br>de goût</p>
  </main>
</body>
</html>
```